Hi! I need an eye catching, clean and bright business card for my cleaning business "Glimmer Rooms by Tova". I specialize in move-out cleans and Real estate listings. I can also do offices. Please make sure viewers are aware that they are looking at a cleaning business card and list my specialties. I don't want it to look too plain and generic; I want it fun and interesting.

I don’t have a logo so you’re free to create any type of card that depicts cleaning. I’m looking for fun and uniqueness!!

REMEMBER… I PREFER A 1 (ONE) SIDED CARD, EVEN THOUGH THE 2 SIDED ONES DO LOOK GREAT.

Thank you all for your participation!! :)

Target Market(s)

Property Management/Rentals & Real Estate Sales Listings.

Industry/Entity Type

Cleaning Company

Contact Information for Business Card

My name - Marisol Dunbarke. Phone number- (555)704-3816. Email Mdunbarke247@mailverity.com Serving Wexbury County and surrounding areas.

Requirements
Must have
• Identify that I'm a cleaning company. Services I offer- Move out/Move in Cleaning, Real Estate Ready Cleans, Office & Commercial Cleaning.
Should not have
• I don't want my home/business address or a website on the card. Only name, phone number, email address and serving counties.

```html
<!DOCTYPE html>
<html lang="en">
<head>
<meta charset="UTF-8">
<title>Glimmer Rooms by Tova — Business Card</title>
<link href="https://fonts.googleapis.com/css2?family=Montserrat:wght@500;600;700&display=swap" rel="stylesheet">
<style>
  :root {
    --stage: #2d2d2f;
    --purple: #5f437f;
    --purple-deep: #4f3570;
    --purple-soft: #7b5fa0;
    --lavender: #e4daf0;
    --white: #ffffff;
    --ink: #2a2236;
  }
  * { box-sizing: border-box; margin: 0; padding: 0; }
  html, body {
    width: 1200px; height: 875px; overflow: hidden;
    background: var(--stage);
    font-family: "Montserrat", Arial, sans-serif;
  }
  .stage {
    width: 1200px; height: 875px;
    display: flex; align-items: center; justify-content: center;
  }
  .card {
    width: 880px; height: 503px;
    border-radius: 28px;
    position: relative; overflow: hidden;
    background: var(--white);
    color: var(--ink);
  }

  /* Services band */
  .services-band {
    position: absolute; left: 0; top: 0; bottom: 0;
    width: 400px;
    background: var(--purple);
    clip-path: polygon(0 0, 100% 0, 82% 100%, 0 100%);
    color: var(--white);
    padding: 0 0 0 44px;
    display: flex; flex-direction: column; justify-content: center;
  }
  .band-accent {
    position: absolute; left: 0; top: 0; bottom: 0; width: 420px;
    pointer-events: none;
  }
  .services-title { font-weight: 700; font-size: 26px; margin-bottom: 18px; }
  .services-list { list-style: none; font-weight: 500; font-size: 18px; line-height: 1.75; }
  .services-list li { display: flex; align-items: center; gap: 12px; }
  .services-list li::before {
    content: ""; width: 9px; height: 9px; border-radius: 50%;
    background: var(--white); flex: none;
  }

  /* Contact side */
  .front-content {
    position: absolute; left: 440px; top: 52px; right: 40px;
  }
  .front-brand {
    color: var(--purple);
    font-weight: 700; font-size: 40px; letter-spacing: 3px;
    text-transform: uppercase; line-height: 1.08;
  }
  .front-brand .by-line {
    display: block; font-size: 22px; letter-spacing: 8px; margin-top: 6px;
  }
  .business-name { margin-top: 28px; color: var(--purple); font-weight: 700; font-size: 24px; }
  .owner-name { font-weight: 500; font-size: 17px; margin-top: 4px; }
  .service-area { font-weight: 500; font-size: 17px; margin-top: 16px; line-height: 1.35; }
  .contact-list { list-style: none; margin-top: 20px; font-weight: 500; font-size: 17px; }
  .contact-list li { display: flex; align-items: center; gap: 12px; line-height: 1.8; }
  .contact-list svg { width: 18px; height: 18px; flex: none; fill: var(--purple); }
</style>
</head>
<body>
<main class="stage">
  <section class="card">
    <svg class="band-accent" viewBox="0 0 420 503" aria-hidden="true">
      <polygon points="400,0 420,0 348,503 328,503" fill="var(--lavender)"/>
    </svg>
    <div class="services-band">
      <h2 class="services-title">Services to Feature</h2>
      <ul class="services-list">
        <li>Move-out / Move-in Cleaning</li>
        <li>Real Estate Ready Cleans</li>
        <li>Office &amp; Commercial Cleaning</li>
      </ul>
    </div>

    <div class="front-content">
      <div class="front-brand">Glimmer<br>Rooms<span class="by-line">by Tova</span></div>
      <div class="business-name">Glimmer Rooms by Tova</div>
      <div class="owner-name">Marisol Dunbarke</div>
      <div class="service-area">Serving Wexbury<br>County &amp; surrounding areas</div>
      <ul class="contact-list">
        <li>
          <svg viewBox="0 0 24 24" aria-hidden="true"><path d="M6.6 10.8a15 15 0 0 0 6.6 6.6l2.2-2.2c.3-.3.7-.4 1-.2 1.1.4 2.3.6 3.6.6.6 0 1 .4 1 1V20c0 .6-.4 1-1 1A17 17 0 0 1 3 4c0-.6.4-1 1-1h3.5c.6 0 1 .4 1 1 0 1.3.2 2.5.6 3.6.1.3 0 .7-.2 1l-2.3 2.2z"/></svg>
          <span>(555)704-3816</span>
        </li>
        <li>
          <svg viewBox="0 0 24 24" aria-hidden="true"><path d="M2 5h20v14H2z" opacity=".35"/><path d="M2 5h20l-10 8z"/></svg>
          <span>Mdunbarke247@mailverity.com</span>
        </li>
      </ul>
    </div>
  </section>
</main>
</body>
</html>
```